PawNook business card

Looking for a fun and cool biz card for a new company with patent pending products. I have products to help and protect dogs hearing. My colors are pantone blue and orange.
Updates

Please add tag line: Protect the ones you love...even your PawNooks!

Target Market(s)

Animal/Dog lovers!

Industry/Entity Type

Retail

Contact Information for Business Card

I'm looking for something simple yet fun with all the info included for biz cards

Colors
0555a3
f78f20

Requirements
Must have
• Logo
Nice to have
• name, website and email
Should not have
• phone number

```html
<!DOCTYPE html>
<html lang="en">
<head>
<meta charset="UTF-8">
<title>PawNook business card</title>
<link href="https://fonts.googleapis.com/css2?family=Poppins:ital,wght@0,500;0,600;0,700&display=swap" rel="stylesheet">
<style>
  :root {
    --brand-blue: #293c85;
    --brand-orange: #f15a24;
    --ink-white: #ffffff;
    --backdrop: #5b5d60;
  }
  * { margin: 0; padding: 0; box-sizing: border-box; }
  html, body {
    width: 1200px;
    height: 1000px;
    overflow: hidden;
    background: var(--backdrop);
    font-family: "Poppins", sans-serif;
  }
  .stage { position: relative; width: 1200px; height: 1000px; }

  .card {
    position: absolute;
    width: 700px;
    height: 400px;
    border-radius: 40px;
    padding: 30px;
  }
  .card__panel {
    width: 100%;
    height: 100%;
    border-radius: 26px;
    display: flex;
    flex-direction: column;
    align-items: center;
    justify-content: center;
  }

  .card--front { left: 130px; top: 60px; background: var(--brand-orange); }
  .card--front .card__panel { background: var(--brand-blue); }

  .card--back { left: 370px; top: 540px; background: var(--brand-blue); }
  .card--back .card__panel { background: var(--brand-orange); }

  .wordmark {
    display: flex;
    align-items: center;
    gap: 16px;
    font-weight: 600;
    font-size: 92px;
    line-height: 1;
    letter-spacing: -1px;
  }
  .wordmark__dot {
    width: 34px;
    height: 34px;
    border-radius: 50%;
  }
  .card--front .wordmark { color: var(--brand-orange); }
  .card--front .wordmark__dot { background: var(--brand-orange); }
  .card--back .wordmark { color: var(--ink-white); font-size: 72px; margin-bottom: 16px; }
  .card--back .wordmark__dot { background: var(--ink-white); width: 28px; height: 28px; }

  .contact {
    color: var(--ink-white);
    text-align: center;
  }
  .contact__name {
    font-weight: 600;
    font-size: 28px;
    line-height: 1.3;
    letter-spacing: 1px;
    margin-bottom: 12px;
  }
  .contact__line {
    font-weight: 500;
    font-size: 19px;
    line-height: 1.5;
  }

  .tagline {
    margin-top: 18px;
    padding-top: 12px;
    border-top: 2px solid var(--ink-white);
    color: var(--ink-white);
    font-weight: 500;
    font-size: 17px;
    line-height: 1.3;
    text-align: center;
    white-space: nowrap;
  }
</style>
</head>
<body>
  <main class="stage">
    <section class="card card--front" aria-label="Business card front">
      <div class="card__panel">
        <div class="wordmark"><span class="wordmark__dot"></span>PawNook</div>
      </div>
    </section>

    <section class="card card--back" aria-label="Business card back">
      <div class="card__panel">
        <div class="wordmark"><span class="wordmark__dot"></span>PawNook</div>
        <div class="contact">
          <p class="contact__name">YOUR NAME</p>
          <p class="contact__line">E-mail : info@pawnook.com</p>
          <p class="contact__line">Web : www.pawnook.com</p>
        </div>
        <p class="tagline">Protect the ones you love...even your PawNooks!</p>
      </div>
    </section>
  </main>
</body>
</html>
```